Legal Recruitment Firm Needs Wordpress Design

We are a legal recruitment firm that represents partner-level attorneys in the top 200 law firms in the world in their move from one law firm to another. I am the founder, and am a twice published author, and I write a column for Counsel Ledger and Varnley.

My site will have 6 "pages" -- Who We Are | What We Do | How We Do It | Why We Are Different | About Our Founder | Contact Us -- and a blog (where I can post my Varnley interviews).

I have attached my logo, and expect that the color/design will follow from that. Where colors are concerned, I like blacks, grays, reds, deep blues, etc.

I'd like to use the Brisk Studio theme -- http://quillpane.example/demo/brisk-studio/

It is fairly simple, I like the full width page display, and I really like the video that plays in the background rather than just a static picture. So I’d like to have a video like this, but perhaps one made of short clips of the streets of NY, London, Hong Kong, etc. (We service attorneys around the world). It wouldn't have to be that, specifically, however -- I will leave the creative aspect up to you.

Please note: (i) I haven't purchased the theme as of yet, so I don't HAVE to use that theme. One that is comparable will do just as fine. Also, (ii) I don't want the typical stock photos of "business people." I really want this to look professional, and think that the stock photos of business people look cheap -- you know, the business websites of the 90's look.

Any photos we would use would have to be fresh, contemporary, and of high quality.

Below are the other themes that I like, and why I like them. I think this will help you to better understand the look/feel that I would like to achieve.

http://quillpane.example/demo/brisk-studio/
-- This is a beautiful theme. And I really like the video in the beginning. I'd love to have a video like this for my page. Perhaps video of the streets of New York, Hong Kong, London, etc? Rather than just a static picture, a video like this?

http://themes.velvorta.example/?theme=LensKip
-- This is another very beautiful theme. I like -- very much -- the simplicity of the blog. The picture is beautiful. I don't think that the picture really caters to my business/industry, but it is amazing. I like the sprawling picture, the easy to follow menu, etc.

http://marqetdepot.example/item/drift-creative-multipurpose-wordpress-theme/full_screen_preview/58204617
-- Another beautiful theme. I really like the sprawling picture. I like the color pallette, as the white letters contrast nicely against it. The menu looks simple. In particular, as you scroll down, I like the video of the New York traffic -- it really adds to the quality, I think.

http://demowp.orbexa.example/tuv/
I like the very clean look of this theme. Only one menu, and that menu only navigates to a single place on the site. The big, full screen, sprawling picture is great, and the font is great. I like the contrast of the white letters against the picture.

http://www.plinthcraft.example/ledges/
-- Not necessarily a great site, but I do like the full-screen picture, and i like the black/gray. I don't like the fonts. I like block lettering with clean, square lines.

http://demo.frovity.example/glidewave-one/
-- I like the big sprawling picture. The colors aren't bad. I like the white contrasting letters. I like that when you scroll down, there is good, clean division between the sections. The clip art of the people looks like, well, clip art. The polished people in suits just looks bad. I really don't like that. The photos should look fresh, contemporary, high def., etc.

http://marqetdepot.zentravo.example/wpversions/harlowe/landing/
-- I like the look of the landing page. This is mainly earth colors -- browns -- which, I want mine to follow the colors of my logo (or contrast in an intelligent way), but I like the big sprawling picture, and the white letters. I like as you scroll down that the division between the sections is more prominent -- you know when you are in a particular "section."

http://demo.parvix-themes.example/otter/
-- I like the look of the landing page, but as you scroll down, it becomes too busy. This may just be because of the content they've put in, though.

Target Market(s)

Partner-level attorneys at the top 200 law firms in the world.

Industry/Entity Type

Law Firm

Number of Pages Required

5+ page

Font styles to use
Sans Serif

Requirements
Must have
• This will be the customization of an existing Wordpress theme, so I expect to receive that -- not simply an adobe mock up.
• Block-style fonts with square edges.
Nice to have
• I've included a significant amount of information in the job description.
Should not have
• Cheap-looking stock photos.

```html
<!DOCTYPE html>
<html lang="en">
<head>
<meta charset="utf-8">
<title>Keelpoint Partner Management</title>
<link rel="stylesheet" href="https://fonts.googleapis.com/css2?family=Open+Sans:ital,wght@0,400;0,600;0,700;0,800;1,400&display=swap">
<style>
:root{
  --ink:#2f2f2f;
  --nav:#2a2a2a;
  --footer:#2b2b2b;
  --footer-base:#222;
  --red:#d9231d;
  --grey-panel:#a9a9a9;
  --dark-panel:#3a3a3a;
  --light-section:#f6f6f6;
  --white:#fff;
  --muted:#9a9a9a;
}
*{margin:0;padding:0;box-sizing:border-box}
html,body{width:1200px;height:2917px;overflow:hidden}
body{position:relative;background:var(--white);font-family:"Open Sans",Arial,sans-serif;color:var(--ink)}
.abs{position:absolute}

/* header */
.site-header{left:0;top:0;width:1200px;height:72px;background:var(--nav)}
.brand{left:43px;top:0;height:72px;display:flex;align-items:center;gap:10px}
.brand-square{width:22px;height:22px;background:var(--red)}
.brand-name{color:var(--white);font-weight:800;font-size:26px;letter-spacing:.5px}
.main-nav{right:93px;top:0;height:72px;display:flex;align-items:center;gap:26px}
.main-nav a{position:relative;color:var(--white);text-decoration:none;font-size:12.5px;font-weight:700;line-height:72px}
.main-nav a.current{color:var(--red)}
.main-nav a.current::before{content:"";position:absolute;left:-4px;right:-4px;top:0;height:4px;background:var(--red)}

/* hero */
.hero{left:0;top:72px;width:1200px;height:780px;background:linear-gradient(180deg,#b9d2e6 0%,#8fa9bf 30%,#74808e 60%,#5d6d82 100%)}
.hero-band{left:0;top:389px;width:1108px;height:210px;background:rgba(160,60,70,.45)}
.hero-title{right:140px;top:393px;color:var(--white);font-weight:800;font-size:118px;line-height:1;letter-spacing:-2px;text-align:right}
.hero-sub{right:142px;top:516px;color:var(--white);font-weight:700;font-size:34px;line-height:1}
.slide-arrow{top:336px;width:38px;height:60px;background:rgba(40,40,40,.55);display:flex;align-items:center;justify-content:center}
.slide-arrow.prev{left:0}
.slide-arrow.next{right:0}

/* welcome */
.welcome{left:88px;top:985px;font-size:76px;font-weight:800;letter-spacing:-1px;line-height:1;color:var(--ink)}

/* tiles */
.tile{overflow:hidden}
.tile-label{position:absolute;color:var(--white);font-weight:700;font-size:28px;line-height:1.2}
.tile-intro{left:0;top:1134px;width:603px;height:263px;background:var(--dark-panel)}
.tile-intro .tile-label{right:25px;top:46px;text-align:right;font-size:35px;line-height:1.3}
.stripe-red{background:var(--red)}
.tile-who{left:615px;top:1134px;width:585px;height:263px;background:linear-gradient(110deg,#f3c48b 0%,#e37d3f 35%,#a3554c 65%,#4b5f8c 100%)}
.tile-who .tile-label{right:20px;bottom:36px}
.tile-how{left:0;top:1397px;width:317px;height:262px;background:var(--grey-panel)}
.tile-how .tile-label{left:81px;bottom:36px}
.tile-walk{left:317px;top:1397px;width:589px;height:262px;background:linear-gradient(180deg,#e9c99c 0%,#b08a68 45%,#3b3430 75%,#5a4a3e 100%);border-top:7px solid var(--red)}
.tile-what{left:906px;top:1397px;width:284px;height:262px;background:var(--grey-panel)}
.tile-what .tile-label{right:22px;bottom:36px}

/* who we are */
.about{left:0;top:1708px;width:1200px;height:445px;background:var(--light-section)}
.about-title{left:105px;top:74px;font-size:52px;font-weight:800;letter-spacing:-.5px;line-height:1}
.about-text{left:107px;top:227px;width:440px;font-size:25px;font-weight:700;line-height:1.25;text-transform:uppercase}
.about-more{left:503px;top:376px;color:var(--red);font-size:23px;font-weight:700;text-decoration:none}
.about-photo{left:718px;top:70px;width:482px;height:330px;background:linear-gradient(160deg,#cfd8dd 0%,#9aa6a8 40%,#5f6b55 75%,#3e4a34 100%)}

/* skyline */
.skyline{left:0;top:2153px;width:1200px;height:483px;background:linear-gradient(180deg,#c9d4da 0%,#9fb0ba 40%,#56687a 75%,#33465a 100%)}

/* footer */
.site-footer{left:0;top:2636px;width:1200px;height:249px;background:var(--footer)}
.footer-brand{left:70px;top:77px;display:flex;align-items:center;gap:10px}
.footer-about{left:301px;top:54px;width:180px;color:var(--muted);font-size:10.5px;font-style:italic;line-height:1.55}
.footer-posts{left:568px;top:52px;width:190px}
.footer-heading{color:var(--white);font-size:11px;font-weight:700;text-transform:uppercase;margin-bottom:13px}
.footer-posts li{list-style:none;color:#cfcfcf;font-size:11px;padding:7px 0 9px;border-bottom:1px solid #555}
.footer-menu{left:850px;top:28px}
.footer-menu li{list-style:none;color:#cfcfcf;font-size:11px;text-transform:uppercase;height:34.5px}
.footer-base{left:0;top:2885px;width:1200px;height:32px;background:var(--footer-base);border-top:1px solid #3c3c3c}
.copyright{left:198px;top:9px;color:#8a8a8a;font-size:9.5px}
.social{left:862px;top:9px;display:flex;gap:20px}
.social span{width:13px;height:13px;border-radius:50%;background:#5a5a5a}
</style>
</head>
<body>

<header class="site-header abs">
  <div class="brand abs"><span class="brand-square"></span><span class="brand-name">KEELPOINT</span></div>
  <nav class="main-nav abs">
    <a class="current" href="#">HOME</a>
    <a href="#">WHO WE ARE</a>
    <a href="#">WHAT WE DO</a>
    <a href="#">HOW WE DO IT</a>
    <a href="#">WHY WE ARE DIFFERENT</a>
    <a href="#">ABOUT OUR FOUNDER</a>
    <a href="#">CONTACT</a>
  </nav>
</header>

<section class="hero abs" role="img" aria-label="Aerial view of a city skyline with skyscrapers under a blue sky">
</section>
<div class="hero-band abs"></div>
<div class="hero-title abs">KEELPOINT</div>
<div class="hero-sub abs">PARTNER MANAGEMENT</div>
<div class="slide-arrow prev abs" style="top:408px">
  <svg width="12" height="20" viewBox="0 0 12 20"><path d="M10 2 2 10l8 8" fill="none" stroke="#fff" stroke-width="2.5"/></svg>
</div>
<div class="slide-arrow next abs" style="top:408px">
  <svg width="12" height="20" viewBox="0 0 12 20"><path d="M2 2l8 8-8 8" fill="none" stroke="#fff" stroke-width="2.5"/></svg>
</div>

<h1 class="welcome abs">WELCOME</h1>

<div class="tile tile-intro abs">
  <p class="tile-label">THANKS FOR STOPPING BY<br>FEEL FREE TO HAVE A<br>LOOK AROUND</p>
</div>
<div class="stripe-red abs" style="left:603px;top:1134px;width:12px;height:263px"></div>
<div class="tile tile-who abs" role="img" aria-label="Light trails of evening traffic through a city street">
  <p class="tile-label">WHO WE ARE</p>
</div>

<div class="tile tile-how abs"><p class="tile-label">HOW WE DO IT</p></div>
<div class="tile tile-walk abs" role="img" aria-label="Silhouetted figures walking along a waterfront promenade at sunrise"></div>
<div class="tile tile-what abs"><p class="tile-label">WHAT WE DO</p></div>
<div class="stripe-red abs" style="left:1190px;top:1397px;width:10px;height:262px"></div>

<section class="about abs">
  <h2 class="about-title abs">WHO WE ARE</h2>
  <p class="about-text abs">We are a group of placement professionals who have made it our business to be experts in the business of law.</p>
  <a class="about-more abs" href="#">FIND OUT MORE...</a>
  <div class="about-photo abs" role="img" aria-label="Historic colonnaded court building among modern towers and trees"></div>
</section>

<section class="skyline abs" role="img" aria-label="Panoramic view of a financial district skyline at dusk"></section>

<footer class="site-footer abs">
  <div class="footer-brand abs"><span class="brand-square"></span><span class="brand-name">KEELPOINT</span></div>
  <p class="footer-about abs">Lorem ipsum ex vix illud nonummy, novum tation et his. At vix scripta patrioque scribentur, at pro fugit erts verterem molestiae, sed et vivendo ali. Lorem ipsum ex vix illud nonummy, novum tation et his. At vix scripta patrioque scribentur...</p>
  <div class="footer-posts abs">
    <p class="footer-heading">Recent Posts</p>
    <ul>
      <li>Voluptas Sadips Ipsums Dolors Untra</li>
      <li>Fugiats Litora Ultrices Ante Auctor</li>
      <li>Sapien Litora Dolors Ultrices</li>
      <li>Nemis Fugiats Voluptas Dolores Uns</li>
    </ul>
  </div>
  <ul class="footer-menu abs">
    <li>Who We Are</li>
    <li>What We Do</li>
    <li>How We Do It</li>
    <li>Why We Are Different</li>
    <li>Our Founder</li>
    <li>Contact Us</li>
  </ul>
</footer>
<div class="footer-base abs">
  <p class="copyright abs">Copyright 2015 Keelpoint | All Rights Reserved</p>
  <div class="social abs"><span></span><span></span><span></span><span></span></div>
</div>

</body>
</html>
```